2 page Web Site Design (Coded), simple, not picky

I need a web portal for a PPC marketing business. I have the logo, some imagery, and some websites to base the design on.

***Background***
The name of the business is "Quiet Harbor Outreach Partners" or QHOP. We provide listings in a searchable database for Dental Sleep Medicine doctors. These are doctors who treat snoring/sleep apnea/and CPAP users with oral appliances. Client doctors will have their own "landing page website" where PPC prospects land from the PPC campaigns. Logos for supporting/landing page websites have been uploaded.
***End Background***

THIS website (for you to design) is to introduce doctors to the concept and detail the services. i.e. PPC campaign management services, listing on a national database of Dental Sleep Medicine practitioners, and a fully featured website dedicated to Snoring, Sleep Apnea, and CPAP Alternative treatment (those websites are "Farewell-Rumble.com", "Farewell-NightPause.com", and ""Farewell-MaskFree.com")

SEM websites whose look I enjoy are:

http://www.brivolta.com/marketing-services/pay-per-click/

http://www.quellandrift.com/welcome/pay-per-click-services/

http://www.tarnolux4co.com/marketing-services/paid-search-management/

The main colors are Red, White, & Blue. Red and blue used mostly for accents/emphasis.

The main/index page's purpose is to, as best possible, convey the idea of SEM campaign management with supporting websites being their best option for internet marketing!
The secondary page is just a slightly modified layout where details can be explained.

Target Market(s)

Dentists who practice Dental Sleep Medicine (see www.pqwrl.org)

Industry/Entity Type

Marketing

Requirements
Must have
• -Sign-up form for the generation of leads... Simple script that sends E-mail is fine... Doctor's Name, Business Name, Business Address, E-mail address, phone #.

-Graphics that will clearly describe the services being provided.

```html
<!DOCTYPE html>
<html lang="en">
<head>
<meta charset="utf-8">
<title>QHOP — Quiet Harbor Outreach Partners</title>
<link rel="stylesheet" href="https://fonts.googleapis.com/css2?family=Oswald:wght@300;400&family=Ubuntu:wght@400;500;700&family=PT+Sans:wght@400;700&family=PT+Sans+Narrow&display=swap">
<style>
:root{
  --red:#b0222c;
  --blue:#2a3f8f;
  --charcoal:#555456;
  --text:#4a4a4a;
  --muted:#8a8a8a;
  --line:#e2e2e2;
  --band:#ebebeb;
  --white:#fff;
}
*{box-sizing:border-box;margin:0;padding:0}
html,body{width:1200px;height:1029px;overflow:hidden;background:var(--white)}
body{position:relative;font-family:"Ubuntu",sans-serif;color:var(--text)}
.abs{position:absolute}

.top-strip{left:171px;top:0;width:858px;height:10px;background:var(--charcoal)}

.brand{left:173px;top:26px;display:flex;align-items:center;gap:8px}
.brand-mark{width:34px;height:34px;border-radius:50%;background:var(--blue)}
.brand-name{font-family:"Ubuntu",sans-serif;font-weight:700;color:var(--red);font-size:32px;line-height:32px;letter-spacing:-0.5px}
.brand-tag{left:174px;top:72px;font-family:"Ubuntu",sans-serif;font-weight:700;color:var(--red);font-size:10px}

.main-nav{right:171px;top:49px;display:flex;gap:24px;font-family:"Oswald",sans-serif;font-weight:300;font-size:13px;letter-spacing:1px;color:var(--muted)}
.main-nav .current{color:var(--red);font-weight:400}

.hero{left:0;top:103px;width:1200px;height:304px;background:linear-gradient(#efefef,#e8e8e8);border-bottom:1px solid #f3f3f3}
.hero-title{left:181px;top:122px;width:440px;white-space:nowrap;font-family:"Oswald",sans-serif;font-weight:300;font-size:39px;line-height:48px;letter-spacing:2.4px;color:#3c3c3c}
.hero-intro{left:183px;top:233px;width:440px;font-size:11px;line-height:22px;letter-spacing:.6px;color:#444}
.hero-points{left:184px;top:294px;list-style:none}
.hero-points li{position:relative;padding-left:16px;height:29px;font-size:10px;font-weight:700;letter-spacing:.7px;color:var(--blue)}
.hero-points li::before{content:"";position:absolute;left:0;top:2px;border-left:7px solid var(--red);border-top:4px solid transparent;border-bottom:4px solid transparent}
.hero-frame{left:639px;top:124px;width:390px;height:260px;background:var(--white);box-shadow:0 1px 3px rgba(0,0,0,.12)}
.hero-photo{left:12px;top:12px;width:365px;height:236px;background:linear-gradient(120deg,#e4ded8,#cfc2b4 45%,#ece9e6)}

.services{left:171px;top:422px;width:858px;height:360px;border:1px solid var(--line);background:var(--white)}
.card{top:27px;width:244px;height:305px;border:1px solid var(--line);border-radius:4px;background:var(--white);box-shadow:0 1px 3px rgba(0,0,0,.08);overflow:hidden}
.card-head{height:38px;background:#f0f0f0;display:flex;align-items:center;gap:10px;padding-left:17px;font-family:"PT Sans Narrow",sans-serif;font-size:14px;letter-spacing:1px;color:#444}
.card-head svg{width:22px;height:22px;fill:#777}
.card-text{padding:12px 15px 0;font-family:"PT Sans",sans-serif;font-size:11px;line-height:19px;letter-spacing:.4px;color:#555}
.card-visual{left:0;top:131px;width:100%;height:123px}
.visual-chart{background:linear-gradient(135deg,#dfe6ef,#b9c7da 55%,#e8edf3)}
.visual-screen{background:linear-gradient(#ececec,#d9d9d9)}
.btn{left:50%;transform:translateX(-50%);top:266px;width:69px;height:27px;background:var(--red);color:var(--white);font-family:"Oswald",sans-serif;font-weight:300;font-size:13px;letter-spacing:1px;display:flex;align-items:center;justify-content:center}
.field{left:13px;width:219px;height:31px;border:1px solid #c9c9c9;border-radius:2px;padding-left:12px;display:flex;align-items:center;font-size:9px;font-style:italic;letter-spacing:.6px;color:var(--blue)}

.partners{left:171px;top:817px;width:858px;height:120px;border:1px solid #dcdcdc;background:repeating-linear-gradient(135deg,#f3f3f3 0 3px,#ececec 3px 6px);display:flex;align-items:center;justify-content:space-around}
.partner{display:flex;align-items:center;gap:8px;font-family:"Ubuntu",sans-serif;font-weight:700;font-size:17px;color:var(--blue)}
.partner-dot{width:26px;height:26px;border-radius:50%;background:var(--blue)}

.footer{left:0;top:980px;width:1200px;height:49px;background:var(--charcoal)}
.footer-mark{left:173px;top:14px;width:22px;height:22px;border-radius:50%;background:#4b67b0}
.copyright{left:215px;top:18px;font-family:"PT Sans Narrow",sans-serif;font-size:10px;letter-spacing:.6px;color:#eee}
.footer-nav{right:171px;top:18px;display:flex;gap:16px;font-family:"PT Sans Narrow",sans-serif;font-size:10px;letter-spacing:.4px;color:#eee}
.footer-nav .current{color:#ff5a5a}
</style>
</head>
<body>
<div class="abs top-strip"></div>

<header>
  <div class="abs brand"><span class="brand-mark"></span><span class="brand-name">QHOP</span></div>
  <div class="abs brand-tag">Quiet Harbor Outreach Partners</div>
  <nav class="abs main-nav">
    <span class="current">HOME</span><span>SERVICES</span><span>CLIENTS</span><span>ABOUT</span><span>BLOG</span><span>CONTACT US</span>
  </nav>
</header>

<section class="abs hero"></section>
<h1 class="abs hero-title">Helping Dental Sleep Doc-<br>tors find their next patient</h1>
<p class="abs hero-intro">Nam est ante, condimentum eu rhoncus sed, egestas a turpis. Phasellus laoreet aliquet odio vitae adipiscing nullam hendrerit dignissim augue .</p>
<ul class="abs hero-points">
  <li>Integer suscipit consequat luctus ellen yellor thenrede illenetery ulle</li>
  <li>Nunc vel purus quam &nbsp;leo convallis id faseter girtey loenerret utlietre</li>
  <li>Vestibulum molestie fermentum purus, et sodales oppertte ono</li>
</ul>
<div class="abs hero-frame"><div class="abs hero-photo" role="img" aria-label="Photo of an older couple smiling at a laptop"></div></div>

<section class="abs services">
  <article class="abs card" style="left:23px">
    <div class="card-head"><svg viewBox="0 0 24 24"><path d="M12 8a4 4 0 1 0 0 8 4 4 0 0 0 0-8zm9 5.5v-3l-2.6-.5a7 7 0 0 0-.8-1.900l1.5-2.2-2.1-2.1-2.2 1.5a7 7 0 0 0-1.9-.8L12.5 2h-3l-.5 2.6a7 7 0 0 0-1.9.8L4.9 3.9 2.8 6l1.5 2.2a7 7 0 0 0-.8 1.9L1 10.5v3l2.6.5c.2.7.4 1.3.8 1.9l-1.5 2.2 2.1 2.1 2.2-1.5c.6.4 1.2.6 1.9.8l.4 2.5h3l.5-2.6c.7-.2 1.3-.4 1.9-.8l2.2 1.5 2.1-2.1-1.5-2.2c.4-.6.6-1.2.8-1.9z"/></svg>LOREM IPSUM CENTARINOS</div>
    <p class="card-text">Cras vel velit mauris. Proin et odio eu dui euismod congue eget et neque. Maecenas lectus magna, dignissim et varius vitae heetore.</p>
    <div class="abs card-visual visual-chart" role="img" aria-label="Photo of a hand pointing at analytics charts on a monitor"></div>
    <a class="abs btn">MORE</a>
  </article>

  <article class="abs card" style="left:308px">
    <div class="card-head"><svg viewBox="0 0 24 24"><path d="M12 2a7 7 0 0 0-4 12.7V17h8v-2.3A7 7 0 0 0 12 2zM9 18h6v1.5H9zm1 2.5h4V22h-4z"/></svg>LOREM IPSUM DOLOMBER</div>
    <p class="card-text">Cras vel velit mauris. Proin et odio eu dui euismod congue eget et neque. Maecenas lectus magna, dignissim et varius vitae heetore.</p>
    <div class="abs card-visual visual-screen" role="img" aria-label="Illustration of a desktop monitor showing search results with pay per click ads highlighted"></div>
    <a class="abs btn">MORE</a>
  </article>

  <article class="abs card" style="left:589px">
    <div class="card-head"><svg viewBox="0 0 24 24"><circle cx="12" cy="7" r="5"/><path d="M2 23c0-6 4-9 10-9s10 3 10 9z"/></svg>SIGN UP TO OUR SERVICE</div>
    <p class="card-text">Cras vel velit mauris. Proin et odio eu dui euismod congue eget et neque.</p>
    <div class="abs field" style="top:107px">Your Name</div>
    <div class="abs field" style="top:158px">Your Email</div>
    <div class="abs field" style="top:210px">Your Phone Number</div>
    <a class="abs btn">MORE</a>
  </article>
</section>

<section class="abs partners">
  <div class="partner"><span class="partner-dot"></span>Farewell-Rumble.com</div>
  <div class="partner"><span class="partner-dot"></span>Farewell-NightPause.com</div>
  <div class="partner"><span class="partner-dot"></span>Farewell-MaskFree.com</div>
</section>

<footer class="abs footer">
  <span class="abs footer-mark"></span>
  <p class="abs copyright">Copyright ©2012 All rights reserved</p>
  <nav class="abs footer-nav"><span class="current">Home</span><span>Services</span><span>Clients</span><span>About</span><span>Blog</span><span>Contact Us</span></nav>
</footer>
</body>
</html>
```